New Business Card Design Project

I would like my card design to look exactly like the logo, design, layout, and print of the current attached file. The only change I would like made would be for the print to say THE KMW GROUP instead of THE HALLORAN GROUP. Basically, just replace his group name with my group name. I would also like the backgroud to be the same texture and color as the attached file. I love the dark blue lettering and house logo on the card.

I am completely open to the rest of the card design. I just want something clean and simple. Only basic contact info required on the card. Maybe just name: Kyle M Warrick and cell # 555.914.2087 and email kyle@orchidhomesagent.com

```html
<!DOCTYPE html>
<html lang="en">
<head>
<meta charset="utf-8">
<title>The KMW Group – Business Card</title>
<link href="https://fonts.googleapis.com/css2?family=Open+Sans:wght@400;800&display=swap" rel="stylesheet">
<style>
  :root {
    --backdrop: #2b2b2d;
    --card-paper: #f3f3f1;
    --ink-navy: #1d1b3b;
    --ink-grey: #8a8a8e;
  }
  * { box-sizing: border-box; margin: 0; padding: 0; }
  html, body {
    width: 1200px;
    height: 900px;
    overflow: hidden;
    background: var(--backdrop);
  }
  .canvas {
    width: 1200px;
    height: 900px;
    display: flex;
    flex-direction: column;
    align-items: center;
    justify-content: center;
    gap: 40px;
  }
  .card {
    width: 700px;
    height: 400px;
    background: var(--card-paper);
    box-shadow: 0 10px 30px rgba(0,0,0,0.45);
    position: relative;
  }
  /* Front: group name */
  .card-front {
    display: flex;
    align-items: center;
    justify-content: center;
  }
  .brand {
    display: flex;
    align-items: center;
    gap: 22px;
  }
  .brand-square {
    width: 52px;
    height: 52px;
    background: var(--ink-navy);
  }
  .brand-name {
    font-family: "Open Sans", sans-serif;
    font-weight: 800;
    font-size: 40px;
    line-height: 1;
    color: var(--ink-navy);
  }
  /* Back: contact */
  .card-back {
    padding: 0 0 0 80px;
    display: flex;
    flex-direction: column;
    justify-content: center;
  }
  .holder-name {
    font-family: "Open Sans", sans-serif;
    font-weight: 800;
    font-size: 54px;
    letter-spacing: 0.01em;
    color: var(--ink-navy);
    line-height: 1;
    margin-top: 90px;
  }
  .holder-contact {
    font-family: "Open Sans", sans-serif;
    font-weight: 400;
    font-size: 14px;
    color: var(--ink-grey);
    margin-top: 12px;
  }
</style>
</head>
<body>
  <main class="canvas">
    <section class="card card-front">
      <div class="brand">
        <div class="brand-square"></div>
        <p class="brand-name">THE KMW GROUP</p>
      </div>
    </section>
    <section class="card card-back">
      <h1 class="holder-name">KYLE M WARRICK</h1>
      <p class="holder-contact">555.914.2087 | kyle@orchidhomesagent.com | orchidhomesagent.com</p>
    </section>
  </main>
</body>
</html>
```